Business Card Design Project : Tidewell Press

In preparation for market launch, Whistler's Tidewell Press require the development of a business card. Tidewell Press is a Community online publishing web portal. We provide the the city of Whistler located in B.C. (Canada) business directories, News, Classified ads, News, Events and blogs etc.

The main focus of the brand is to help local businesses to corporate with their online advertisement and marketing. Meeting our clients face to face is a must (B2B).

Target Market(s)

The target market is B2B customers. Business Owners to Marketing, advertising Managers

Industry/Entity Type

Business

Requirements
Must have
• - The business card will be two sided.
the BACK side will have our logo which consist of (icon, url,slogan) submited. The logo will be middle and centred.

The FRONT side should have company details:

Company Legal Name: FERNDALE TIDEWELL PRESS

Owen Marsk
Director of Sales & Marketing

www.ferndaletidewell.biz
owen@ferndaletidewell.biz

Phone: 555 014 3826
#2817 - 562 E. Harlow Ave.
Vancouver, B.C. K7P2R4 Canada
Nice to have
• - For the "FRONT" side of our business card. You can separate or re-arrange with our logo components (icon, logo,slogan). It does not have to be together.

Also our company legal name is rather long so arrange or organize the name in a way to make it shorter. Your experience and creativity will have to come in play.
Should not have
• should not have other colors beside logo color and black text (2 colors). Also nothing Three dimensional

```html
<!DOCTYPE html>
<html lang="en">
<head>
<meta charset="utf-8">
<title>Tidewell Press – Business Card</title>
<link rel="stylesheet" href="https://fonts.googleapis.com/css2?family=Source+Sans+3:wght@400;600;700&family=Arimo:wght@400&display=swap">
<style>
  :root {
    --brand-blue: #0a7ccf;
    --ink: #111111;
    --paper: #ffffff;
    --stage: #e9e9e9;
    --watermark: #ececec;
  }
  * { box-sizing: border-box; margin: 0; padding: 0; }
  html, body { width: 1200px; height: 1000px; overflow: hidden; }
  body {
    background: var(--stage);
    font-family: "Source Sans 3", "Myriad Pro", sans-serif;
    position: relative;
  }

  .card { position: absolute; overflow: hidden; }

  /* Back side */
  .card-back {
    left: 49px; top: 32px; width: 748px; height: 443px;
    background: var(--brand-blue);
    box-shadow: 0 4px 14px rgba(0,0,0,.25);
  }
  .card-back .brand-lockup {
    position: absolute; left: 0; right: 0; top: 120px;
    text-align: center;
  }
  .card-back .brand-name {
    display: inline-flex; align-items: center; gap: 16px;
    color: var(--paper); font-weight: 700; font-size: 62px; line-height: 1;
  }
  .card-back .brand-dot {
    width: 30px; height: 30px; border-radius: 50%; background: var(--paper);
  }
  .card-back .brand-url {
    margin-top: 44px;
    color: var(--ink); font-weight: 700; font-size: 36px; line-height: 1;
  }
  .card-back .brand-slogan {
    margin-top: 8px;
    color: var(--paper); font-size: 28px; line-height: 1;
  }

  /* Front side */
  .card-front {
    left: 393px; top: 507px; width: 750px; height: 442px;
    background: var(--paper);
    box-shadow: 0 4px 14px rgba(0,0,0,.25);
  }
  .card-front .watermark-name {
    position: absolute; left: 150px; top: 200px;
    color: var(--watermark); font-weight: 700; font-size: 92px; line-height: 1;
    white-space: nowrap;
  }
  .card-front .brand-lockup {
    position: absolute; right: 23px; top: 22px; text-align: center;
  }
  .card-front .brand-name {
    display: inline-flex; align-items: center; gap: 8px;
    color: var(--brand-blue); font-weight: 700; font-size: 34px; line-height: 1;
  }
  .card-front .brand-dot {
    width: 14px; height: 14px; border-radius: 50%; background: var(--brand-blue);
  }
  .card-front .brand-url {
    margin-top: 34px;
    color: var(--ink); font-weight: 700; font-size: 21px; line-height: 1;
  }
  .card-front .brand-slogan {
    margin-top: 3px;
    color: var(--brand-blue); font-size: 16px; line-height: 1;
  }

  .address {
    position: absolute; left: 35px; top: 148px;
    color: var(--ink); font-size: 20px; line-height: 28px; font-style: normal;
  }
  .contact-list {
    position: absolute; left: 35px; top: 240px; list-style: none;
    color: var(--ink); font-size: 20px;
  }
  .contact-list li { display: flex; align-items: center; gap: 6px; height: 32px; }
  .contact-list li.group-gap { margin-top: 27px; }
  .contact-list svg { width: 20px; height: 20px; fill: var(--brand-blue); flex: none; }

  .person {
    position: absolute; right: 42px; top: 246px; text-align: right;
  }
  .person-name {
    font-family: "Arimo", Arial, sans-serif;
    color: var(--brand-blue); font-size: 50px; font-weight: 400; line-height: 1;
  }
  .person-title {
    margin-top: 8px; color: var(--ink); font-size: 20px; line-height: 1;
  }

  .footer-band { position: absolute; left: 0; bottom: 0; width: 750px; height: 60px; }
</style>
</head>
<body>

<section class="card card-back" aria-label="Business card, back side">
  <div class="brand-lockup">
    <div class="brand-name"><span class="brand-dot"></span>Tidewell Press</div>
    <div class="brand-url">www.ferndaletidewell.biz</div>
    <div class="brand-slogan">Your information gateway</div>
  </div>
</section>

<section class="card card-front" aria-label="Business card, front side">
  <div class="watermark-name" aria-hidden="true">Tidewell Press</div>

  <div class="brand-lockup">
    <div class="brand-name"><span class="brand-dot"></span>Tidewell Press</div>
    <div class="brand-url">www.ferndaletidewell.biz</div>
    <div class="brand-slogan">Your information gateway</div>
  </div>

  <address class="address">
    #2817 - 562 E. Harlow Ave.<br>
    Vancouver, B.C. K7P2R4 Canada
  </address>

  <ul class="contact-list">
    <li>
      <svg viewBox="0 0 24 24" aria-hidden="true"><path d="M6.6 10.8a15.1 15.1 0 0 0 6.6 6.6l2.2-2.2c.3-.3.7-.4 1-.2 1.1.4 2.3.6 3.6.6.6 0 1 .4 1 1V20c0 .6-.4 1-1 1A17 17 0 0 1 3 4c0-.6.4-1 1-1h3.5c.6 0 1 .4 1 1 0 1.3.2 2.5.6 3.6.1.3 0 .7-.2 1l-2.3 2.2z"/></svg>
      555 014 3826
    </li>
    <li>
      <svg viewBox="0 0 24 24" aria-hidden="true"><path d="M8 2h8a2 2 0 0 1 2 2v16a2 2 0 0 1-2 2H8a2 2 0 0 1-2-2V4a2 2 0 0 1 2-2zm0 3v11h8V5H8zm4 13a1.2 1.2 0 1 0 0 2.4A1.2 1.2 0 0 0 12 18z"/></svg>
      +00(0)0 00000000
    </li>
    <li class="group-gap">
      <svg viewBox="0 0 24 24" aria-hidden="true"><path d="M2 6a2 2 0 0 1 2-2h16a2 2 0 0 1 2 2v12a2 2 0 0 1-2 2H4a2 2 0 0 1-2-2V6zm2 .5V7l8 5.5L20 7v-.5H4zM4 9.4V17.5h16V9.4l-8 5.5-8-5.5z"/></svg>
      owen@ferndaletidewell.biz
    </li>
    <li>
      <svg viewBox="0 0 24 24" aria-hidden="true"><path d="M12 2a10 10 0 1 0 0 20 10 10 0 0 0 0-20zm6.9 9h-3a15 15 0 0 0-1.2-5.6A8 8 0 0 1 18.9 11zM12 4.1c.9 1.2 1.8 3.6 1.9 6.9h-3.8c.1-3.3 1-5.7 1.9-6.9zM9.3 5.4A15 15 0 0 0 8.1 11h-3a8 8 0 0 1 4.2-5.6zM5.1 13h3a15 15 0 0 0 1.2 5.6A8 8 0 0 1 5.1 13zm6.9 6.9c-.9-1.2-1.8-3.6-1.9-6.9h3.8c-.1 3.3-1 5.7-1.9 6.9zm2.7-1.3a15 15 0 0 0 1.2-5.6h3a8 8 0 0 1-4.2 5.6z"/></svg>
      www.ferndaletidewell.biz
    </li>
  </ul>

  <div class="person">
    <div class="person-name">Owen Marsk</div>
    <div class="person-title">Director of Sales &amp; Marketing</div>
  </div>

  <svg class="footer-band" viewBox="0 0 750 60" aria-hidden="true">
    <rect x="0" y="23" width="750" height="28" fill="var(--ink)"/>
    <path d="M390 51 C400 10 410 6 440 6 L750 6 L750 51 Z" fill="var(--brand-blue)"/>
  </svg>
</section>

</body>
</html>
```